Brixel Information Technology Solutions
We are an Information Technology Company. We provide computer services to commercial companies. We would like a new card full color front and back with bleeding edge.
We have a logo that you can use or if you want to come up with a new logo that is fine too.
Our colors are mostly Maroon and black but be creative.
Sample Information
Grant P Oswick
4818 W Saguaro Ridge Drive
Suite 410
Tempe, AZ 85281
O: 602.555.0143
C: 602.555.0178
24/7: 888.555.0162
goswick@brixelit.com
www.brixelit.com
Target Market(s)
Business of all sizes
Industry/Entity Type
Computer
Requirements
Must have
- Bleeding edge
full color on both sides

```html
<!DOCTYPE html>
<html lang="en">
<head>
<meta charset="UTF-8">
<title>Brixel Information Technology Solutions — Business Card</title>
<link href="https://fonts.googleapis.com/css2?family=Arimo:wght@400;700&family=Open+Sans:wght@300;400&display=swap" rel="stylesheet">
<style>
  :root {
    --maroon: #7a1a24;
    --maroon-mid: #6a1720;
    --maroon-deep: #4a1218;
    --black: #000000;
    --white: #ffffff;
    --soft-white: #e9e9e9;
    --canvas: #ececec;
    --brand-square: #a3202c;
  }
  * { margin: 0; padding: 0; box-sizing: border-box; }
  html, body {
    width: 1200px;
    height: 2900px;
    overflow: hidden;
    background: var(--canvas);
  }
  .sheet {
    width: 1200px;
    height: 2900px;
    display: flex;
    flex-direction: column;
    align-items: center;
    justify-content: center;
    gap: 180px;
  }
  .card {
    position: relative;
    width: 1000px;
    height: 572px;
    overflow: hidden;
    font-family: "Arimo", Arial, sans-serif;
    color: var(--white);
  }
  .card--front {
    background: linear-gradient(135deg, var(--maroon) 0%, var(--maroon-mid) 55%, var(--maroon-deep) 100%);
  }
  .card--back {
    background: var(--black);
  }
  .brand {
    display: flex;
    align-items: center;
    gap: 10px;
  }
  .brand__square {
    width: 22px;
    height: 22px;
    background: var(--brand-square);
  }
  .brand__name {
    font-weight: 700;
    font-size: 26px;
    line-height: 30px;
    letter-spacing: 3px;
    color: var(--white);
  }
  .card--front .brand {
    position: absolute;
    left: 82px;
    top: 200px;
  }
  .front__company {
    position: absolute;
    left: 82px;
    top: 246px;
    font-weight: 700;
    font-size: 34px;
    line-height: 40px;
    letter-spacing: 0.3px;
    white-space: nowrap;
  }
  .card--back .brand {
    position: absolute;
    left: 104px;
    top: 150px;
  }
  .address {
    position: absolute;
    left: 104px;
    top: 200px;
    font-style: normal;
    font-size: 24px;
    line-height: 36px;
    white-space: nowrap;
  }
  .phones {
    position: absolute;
    left: 104px;
    top: 340px;
    font-size: 24px;
    line-height: 48px;
    white-space: nowrap;
  }
  .contact {
    position: absolute;
    right: 60px;
    top: 90px;
    text-align: right;
    white-space: nowrap;
  }
  .contact__name {
    font-weight: 700;
    font-size: 34px;
    line-height: 40px;
  }
  .contact__title {
    font-family: "Open Sans", Arial, sans-serif;
    font-weight: 300;
    font-size: 22px;
    letter-spacing: 1px;
    color: var(--soft-white);
    margin-bottom: 30px;
  }
  .contact__label {
    font-family: "Open Sans", Arial, sans-serif;
    font-weight: 300;
    font-size: 20px;
    letter-spacing: 1px;
    color: var(--soft-white);
    line-height: 26px;
  }
  .contact__value {
    font-size: 22px;
    line-height: 28px;
    margin-bottom: 22px;
  }
  .contact__web {
    font-weight: 700;
    font-size: 30px;
    line-height: 36px;
  }
</style>
</head>
<body>
<main class="sheet">
  <section class="card card--front" aria-label="Card front">
    <div class="brand">
      <span class="brand__square"></span>
      <span class="brand__name">BRIXEL</span>
    </div>
    <h1 class="front__company">Brixel Information Technology Solutions</h1>
  </section>

  <section class="card card--back" aria-label="Card back">
    <div class="brand">
      <span class="brand__square"></span>
      <span class="brand__name">BRIXEL</span>
    </div>
    <address class="address">
      4818 W Saguaro Ridge Drive<br>
      Suite 410<br>
      Tempe, AZ 85281
    </address>
    <div class="phones">
      <div>O : 602.555.0143</div>
      <div>C : 602.555.0178</div>
    </div>
    <div class="contact">
      <div class="contact__name">Grant P Oswick</div>
      <div class="contact__title">DIRECTOR</div>
      <div class="contact__label">24/7</div>
      <div class="contact__value">888.555.0162</div>
      <div class="contact__label">EMAIL</div>
      <div class="contact__value">goswick@brixelit.com</div>
      <div class="contact__label">WEBSITE</div>
      <div class="contact__web">www.brixelit.com</div>
    </div>
  </section>
</main>
</body>
</html>
```